Bref créative
Business Cards & Letterhead for a business that owns franchises
HARTWELL HOLDINGS GROUP
Professional
Gregory T. Pennock, Sr.
President & Co-Owner
3852 Fernhollow Bend, SE
Atlanta, GA
Gregory@HartHoldingsGroup.example
www.hartholdingsgroup.example
Our Logo? Be Creative!!
HARTWELL HOLDINGS GROUP LOGO

```html
<!DOCTYPE html>
<html lang="en">
<head>
<meta charset="utf-8">
<title>Hartwell Holdings Group – Business Card</title>
<link href="https://fonts.googleapis.com/css2?family=Cormorant+SC:wght@500;600&display=swap" rel="stylesheet">
<style>
  :root {
    --backdrop: #e6e4e1;
    --card-white: #ffffff;
    --brand-red: #d42a2f;
    --brand-red-deep: #b81f25;
    --divider-grey: #8f9093;
    --ink-light: #ffffff;
  }
  * { margin: 0; padding: 0; box-sizing: border-box; }
  html, body {
    width: 1200px; height: 914px; overflow: hidden;
    background: var(--backdrop);
    font-family: "Cormorant SC", Georgia, serif;
  }
  .canvas {
    position: relative; width: 1200px; height: 914px;
    display: flex; align-items: center; justify-content: center;
  }
  .business-card {
    position: relative; width: 1000px; height: 571px;
    background: var(--card-white);
    box-shadow: 0 6px 22px rgba(0,0,0,.18);
    overflow: hidden;
  }
  .card-shapes { position: absolute; inset: 0; }
  .holder-name {
    position: absolute; left: 48px; top: 40px;
    color: var(--ink-light); font-size: 30px; font-weight: 500; letter-spacing: .5px;
  }
  .holder-title {
    position: absolute; left: 48px; top: 80px;
    color: var(--ink-light); font-size: 20px; font-weight: 500; letter-spacing: .5px;
  }
  .contact-list {
    position: absolute; left: 48px; top: 230px; list-style: none;
    color: var(--ink-light); font-size: 17px; font-weight: 500; line-height: 22px;
  }
  .contact-list li { display: flex; align-items: flex-start; gap: 12px; margin-bottom: 8px; }
  .contact-icon { flex: none; width: 18px; height: 18px; margin-top: 2px; }
  .brand-lockup {
    position: absolute; left: 520px; top: 248px;
    display: flex; align-items: center; gap: 22px;
  }
  .brand-circle {
    width: 110px; height: 110px; border-radius: 50%;
    border: 5px solid var(--brand-red);
  }
  .brand-name {
    color: var(--brand-red); font-weight: 600; font-size: 40px;
    line-height: 40px; letter-spacing: 1px;
  }
</style>
</head>
<body>
<main class="canvas">
  <article class="business-card">
    <svg class="card-shapes" viewBox="0 0 1000 571" width="1000" height="571" aria-hidden="true">
      <path class="divider-band" d="M640,0 C505,130 420,330 400,571 H372 C392,330 480,125 612,0 Z" fill="var(--divider-grey)"/>
      <path class="red-field" d="M0,0 H600 C470,125 385,330 362,571 H0 Z" fill="var(--brand-red)"/>
    </svg>

    <h1 class="holder-name">Gregory T. Pennock, Sr.</h1>
    <p class="holder-title">President &amp; Co-Owner</p>

    <ul class="contact-list">
      <li>
        <svg class="contact-icon" viewBox="0 0 18 18"><circle cx="9" cy="9" r="9" fill="#fff"/><path d="M9 4a3 3 0 0 1 3 3c0 2.3-3 6-3 6s-3-3.7-3-6a3 3 0 0 1 3-3z" fill="var(--brand-red)"/><circle cx="9" cy="7" r="1.1" fill="#fff"/></svg>
        <span>3852 Fernhollow Bend, SE Atlanta, GA<br>30317</span>
      </li>
      <li>
        <svg class="contact-icon" viewBox="0 0 18 18"><circle cx="9" cy="9" r="9" fill="#fff"/><path d="M5.5 5c.6-.6 1.3-.5 1.6 0l1 1.6c.3.5.1 1-.3 1.3l-.5.4c.5 1.1 1.3 1.9 2.4 2.4l.4-.5c.3-.4.8-.6 1.3-.3l1.6 1c.5.3.6 1 0 1.6-2.6 2.1-9.6-4.9-7.5-7.5z" fill="var(--brand-red)"/></svg>
        <span>555.014.2287 | 555.018.3341</span>
      </li>
      <li>
        <svg class="contact-icon" viewBox="0 0 18 18"><circle cx="9" cy="9" r="9" fill="#fff"/><rect x="6.3" y="4" width="5.4" height="10" rx="1" fill="var(--brand-red)"/><rect x="7.2" y="5.2" width="3.6" height="6.4" fill="#fff"/></svg>
        <span>555.017.6620</span>
      </li>
      <li>
        <svg class="contact-icon" viewBox="0 0 18 18"><circle cx="9" cy="9" r="9" fill="#fff"/><rect x="4.5" y="5.8" width="9" height="6.4" fill="var(--brand-red)"/><path d="M4.5 5.8 9 9.4l4.5-3.6" fill="none" stroke="#fff" stroke-width="1"/></svg>
        <span>Gregory@HartHoldingsGroup.example</span>
      </li>
    </ul>

    <div class="brand-lockup">
      <div class="brand-circle"></div>
      <p class="brand-name">HARTWELL<br>HOLDINGS GROUP</p>
    </div>
  </article>
</main>
</body>
</html>
```